Public Adjuster mailing campaign

We are public insurance adjusters. When people (the insured) are not being paid fairly on their insurance claim, we help them get paid all they are owed according to their coverage.We would like a post card mailer to send to homes that have been damaged by a recent tornado. I would like to say something like...Storm Damage?Is your insurance paying everything you are owed?You have rights!Get a FREE claim review!CALL NOW!972-954-6845ADJUSTER FOR THE INSUREDI would like to see a photo in the back ground of a damaged home. I would like a design on both sides of the post card.Colors I prefer are navy as a base color and white text ( or red text for the CALL NOW and the phone number.I would like the message to communicate I am a licensed public adjuster working for the insured and I can help them get what they are owed from the insurance company.

```html
<!DOCTYPE html>
<html lang="en">
<head>
<meta charset="utf-8">
<title>Storm Damage Postcard – Adjuster for the Insured</title>
<link rel="stylesheet" href="https://fonts.googleapis.com/css2?family=Bebas+Neue&family=Roboto:wght@300;400;500;700&display=swap">
<style>
  :root {
    --canvas-bg: #a6a6a6;
    --navy: #1f2d45;
    --navy-panel: rgba(22, 33, 55, 0.82);
    --strip-gray: #3a3d42;
    --band-dark: #2b2b2d;
    --band-black: #1a1b1e;
    --alert-red: #ee2224;
    --white: #ffffff;
    --rule: #1a1a1a;
    --sky: #4a86c6;
    --roof: #a46a38;
    --grass: #3f7a34;
  }
  * { box-sizing: border-box; margin: 0; padding: 0; }
  html, body { width: 988px; height: 1200px; overflow: hidden; }
  body { background: var(--canvas-bg); font-family: "Roboto", Arial, sans-serif; color: var(--white); position: relative; }

  .postcard { position: absolute; left: 159px; width: 753px; height: 541px; overflow: hidden; box-shadow: 4px 5px 8px rgba(0,0,0,0.35); }
  .postcard--front { top: 44px; }
  .postcard--back { top: 614px; background: var(--white); }

  .photo { position: absolute; }
  .photo--front { inset: 0; background: linear-gradient(180deg, var(--sky) 0%, #6f8fb0 22%, #8a6a4a 45%, #5a5048 70%, #3a3a3a 100%); }
  .photo--back { left: 0; top: 0; width: 417px; height: 541px;
    background: linear-gradient(180deg, #1d2c47 0%, #2c4466 30%, #3b4f6c 50%, #2c3346 68%, var(--grass) 82%, #2a4a2a 100%); }

  .headline { font-family: "Bebas Neue", Impact, sans-serif; font-weight: 400; line-height: 1; position: absolute; white-space: nowrap; }
  .subline { font-weight: 300; position: absolute; white-space: nowrap; line-height: 1; }
  .subline strong { font-weight: 700; }

  /* Front */
  .front-panel { position: absolute; left: 0; top: 207px; width: 620px; height: 216px; background: var(--navy-panel); }
  .front-title { left: 46px; top: 232px; font-size: 91px; }
  .front-question { left: 47px; top: 336px; font-size: 22px; }
  .front-rights { left: 49px; top: 366px; font-size: 47px; }
  .front-strip { position: absolute; left: 0; top: 423px; width: 753px; height: 57px; }
  .front-review { left: 46px; top: 443px; font-size: 21px; }
  .front-call { left: 402px; top: 431px; font-size: 48px; }
  .front-phone { position: absolute; right: 28px; top: 443px; font-size: 23px; font-weight: 400; line-height: 1; }
  .front-band { position: absolute; left: 0; top: 480px; width: 753px; height: 61px; background: var(--band-dark); }
  .tagline { position: absolute; font-weight: 500; letter-spacing: 0.2px; white-space: nowrap; line-height: 1; }
  .front-tagline { right: 28px; top: 498px; font-size: 22px; }

  /* Back */
  .back-title { left: 16px; top: 36px; font-size: 59px; }
  .back-question { left: 18px; top: 95px; font-size: 16.5px; }
  .back-rights { left: 75px; top: 210px; font-size: 50px; }
  .back-review { left: 76px; top: 268px; font-size: 21px; }
  .back-callbox { position: absolute; left: 198px; top: 335px; width: 219px; height: 110px; background: var(--alert-red); }
  .back-call { left: 217px; top: 349px; font-size: 55px; }
  .back-phone { position: absolute; left: 220px; top: 405px; font-size: 23px; line-height: 1; }
  .back-band { position: absolute; left: 0; top: 487px; width: 417px; height: 54px; }
  .back-tagline { left: 0; width: 417px; text-align: center; top: 500px; font-size: 19.5px; }

  .address-side { position: absolute; left: 417px; top: 0; width: 336px; height: 541px; }
</style>
</head>
<body>

<section class="postcard postcard--front" aria-label="Postcard front">
  <div class="photo photo--front" role="img" aria-label="Photo of a tornado-damaged white house with torn roof shingles under a blue sky"></div>
  <div class="front-panel"></div>
  <h1 class="headline front-title">STORM DAMAGE?</h1>
  <p class="subline front-question">Is your insurance paying everything you are owed?</p>
  <p class="headline front-rights">YOU HAVE RIGHTS!</p>

  <svg class="front-strip" viewBox="0 0 753 57" width="753" height="57" aria-hidden="true">
    <rect x="0" y="0" width="753" height="57" fill="var(--alert-red)"/>
    <polygon points="0,0 354,0 381,28.5 354,57 0,57" fill="var(--strip-gray)"/>
  </svg>
  <p class="subline front-review">Get a <strong>FREE</strong> claim review!</p>
  <p class="headline front-call">CALL NOW!</p>
  <p class="front-phone">815-372-4091</p>

  <div class="front-band"></div>
  <p class="tagline front-tagline">ADJUSTER FOR THE INSURED</p>
</section>

<section class="postcard postcard--back" aria-label="Postcard back">
  <div class="photo photo--back" role="img" aria-label="Photo of a house with a collapsed roof after a tornado, debris on the lawn at dusk"></div>
  <h2 class="headline back-title">STORM DAMAGE?</h2>
  <p class="subline back-question">Is your insurance paying everything you are owed?</p>
  <p class="headline back-rights">YOU HAVE RIGHTS!</p>
  <p class="subline back-review">Get a <strong>FREE</strong> claim review!</p>

  <div class="back-callbox"></div>
  <p class="headline back-call">CALL NOW!</p>
  <p class="back-phone">815-372-4091</p>

  <svg class="back-band" viewBox="0 0 417 54" width="417" height="54" aria-hidden="true">
    <polygon points="28,0 384,0 417,54 0,54" fill="var(--band-black)"/>
  </svg>
  <p class="tagline back-tagline">ADJUSTER FOR THE INSURED</p>

  <svg class="address-side" viewBox="0 0 336 541" width="336" height="541" aria-label="Address area">
    <rect x="203" y="28" width="104" height="104" fill="none" stroke="var(--rule)" stroke-width="1.2"/>
    <g stroke="var(--rule)" stroke-width="1.2">
      <line x1="0" y1="180" x2="322" y2="180"/>
      <line x1="0" y1="217" x2="322" y2="217"/>
      <line x1="0" y1="254" x2="322" y2="254"/>
      <line x1="0" y1="290" x2="322" y2="290"/>
    </g>
  </svg>
</section>

</body>
</html>
```